Overhaul Powerpoint presentation

I'd like to refresh it with new images where appropriate, new design per slide with same content and utilize the brand colors for my company; Brevan Corelink. This is an internal interview deck for a VP role at my company.

```html
<!DOCTYPE html>
<html lang="en">
<head>
<meta charset="utf-8">
<title>Leadership Philosophy – Key Capabilities</title>
<link href="https://fonts.googleapis.com/css2?family=Open+Sans:ital,wght@0,300;0,400;0,600;1,300&display=swap" rel="stylesheet">
<style>
  :root {
    --bg: #f2f3f4;
    --brand-blue: #1aa0dc;
    --text-grey: #4f5458;
    --muted-grey: #6b7075;
    --rule-grey: #d5d8db;
    --tile-blue: #0b96d6;
    --tile-green: #a6bf2f;
    --tile-teal: #0f6b76;
    --tile-dark: #0c393f;
    --white: #ffffff;
  }
  * { margin: 0; padding: 0; box-sizing: border-box; }
  html, body { width: 1200px; height: 900px; overflow: hidden; }
  body {
    font-family: "Open Sans", Arial, sans-serif;
    background: var(--bg);
  }
  .slide {
    position: relative;
    width: 1200px;
    height: 900px;
    background: var(--bg);
  }
  .slide-header {
    position: absolute;
    left: 40px;
    top: 34px;
    width: 1120px;
    height: 70px;
    display: flex;
    align-items: center;
    justify-content: space-between;
    border-bottom: 3px solid var(--brand-blue);
  }
  .slide-title {
    font-size: 40px;
    font-weight: 400;
    color: var(--brand-blue);
    line-height: 60px;
  }
  .brand-mark {
    display: flex;
    align-items: center;
    gap: 10px;
    font-size: 26px;
    font-weight: 600;
    color: var(--brand-blue);
  }
  .brand-mark .square {
    width: 16px;
    height: 16px;
    background: var(--brand-blue);
  }

  /* Left column */
  .quote-block {
    position: absolute;
    left: 40px;
    top: 140px;
    width: 520px;
    padding-left: 24px;
    border-left: 6px solid var(--tile-green);
  }
  .quote-text {
    font-size: 25px;
    line-height: 38px;
    font-weight: 300;
    font-style: italic;
    color: var(--text-grey);
  }
  .quote-source {
    margin-top: 14px;
    font-size: 18px;
    font-weight: 600;
    color: var(--muted-grey);
  }
  .photo-grid {
    position: absolute;
    left: 40px;
    top: 470px;
    width: 520px;
    height: 350px;
    display: grid;
    grid-template-columns: 1fr 1fr;
    grid-template-rows: 210px 130px;
    gap: 10px;
  }
  .photo--volunteers {
    grid-column: 1 / 3;
    background: linear-gradient(160deg, #c9ccd0 0%, #8a8f94 45%, #3c3b3d 100%);
  }
  .photo--presenting {
    background: linear-gradient(180deg, #d8cdb8 0%, #b9a98c 55%, #4a3d33 100%);
  }
  .photo--team {
    background: linear-gradient(180deg, #c8d7e6 0%, #9aa8a8 45%, #6f7a86 100%);
  }

  /* Right column */
  .section-heading {
    position: absolute;
    left: 600px;
    top: 128px;
    width: 560px;
    font-size: 56px;
    line-height: 80px;
    font-weight: 300;
    color: var(--text-grey);
  }
  .capabilities {
    position: absolute;
    left: 600px;
    top: 240px;
    width: 560px;
    height: 580px;
    display: grid;
    grid-template-columns: 1fr 1fr;
    grid-template-rows: 1fr 1fr;
    gap: 10px;
  }
  .capability {
    display: flex;
    align-items: center;
    justify-content: center;
    text-align: center;
    color: var(--white);
    font-size: 38px;
    line-height: 48px;
    font-weight: 400;
  }
  .capability--blue { background: var(--tile-blue); }
  .capability--green { background: var(--tile-green); }
  .capability--teal { background: var(--tile-teal); }
  .capability--dark { background: var(--tile-dark); }

  .footer {
    position: absolute;
    left: 40px;
    top: 848px;
    width: 1120px;
    padding-top: 12px;
    border-top: 1px solid var(--rule-grey);
    text-align: center;
    font-size: 15px;
    color: var(--muted-grey);
  }
</style>
</head>
<body>
  <main class="slide">
    <header class="slide-header">
      <h1 class="slide-title">Leadership Philosophy</h1>
      <div class="brand-mark"><span class="square"></span>Brevan Corelink</div>
    </header>

    <blockquote class="quote-block">
      <p class="quote-text">"Great leaders are almost always great simplifiers, who can cut through argument, debate and doubt to offer a solution everybody can understand."</p>
      <p class="quote-source">– Marcus Delane</p>
    </blockquote>

    <section class="photo-grid">
      <div class="photo photo--volunteers" role="img" aria-label="Photo of a volunteer team in hard hats at a home-building site"></div>
      <div class="photo photo--presenting" role="img" aria-label="Photo of two colleagues in a lively discussion at a meeting"></div>
      <div class="photo photo--team" role="img" aria-label="Group photo of a leadership team outdoors on a terrace"></div>
    </section>

    <h2 class="section-heading">Key Capabilities</h2>

    <section class="capabilities">
      <div class="capability capability--blue">Sense<br>making</div>
      <div class="capability capability--green">Relating</div>
      <div class="capability capability--teal">Visioning</div>
      <div class="capability capability--dark">Inventing</div>
    </section>

    <footer class="footer">© 2017. Brevan Corelink, Inc. All rights reserved.</footer>
  </main>
</body>
</html>
```